Redhollow Balloon Festival web site design

"Redhollow" Annual Hot Air Balloon Festival. Be sure to spell Balloon proprely! The largest in the state of Texas. In a park setting with sky divers, live concerts, 5K run event, kids fun zones, food vendors, merchandise, fireowrks, arts & crafts, family oriented, very colorful. Would like to establish themselves as the only event of it's kind in the region. Would like to convey that the event is very cost friendly and a unique experience relative to the other family entertainment opportunities in the area. Easy to read! Would like to emulate various features of www.updraftjubilee.com

Target Market(s)

Families. Kids up to 12. Then adults 25 to 80.

Industry/Entity Type

Entertainment

Requirements
Must have
• Ease of use for participants. There will be an area dedicated to each of the following categories: Attendees, Pilots, Vendors, Volunteers, Performers. Directions, event schedule and tickets will be critical call outs. Then details and sign up info for the other 4 categories. Will need a register/login feature.
Nice to have
• Weather conditions feature, countdown to event clock, social media integration to home page, youtube channel with videos of launch, custom static background image to frame header and content area.
Should not have
• Dark dreary colors or hard to read fonts.

```html
<!DOCTYPE html>
<html lang="en">
<head>
<meta charset="utf-8">
<title>Redhollow Balloon Festival</title>
<link rel="stylesheet" href="https://fonts.googleapis.com/css2?family=Arimo:wght@400;700&family=Archivo+Narrow:wght@400;700&family=Lora:ital@1&display=swap">
<style>
:root{
  --sky-top:#a9c6e6;
  --sky-bottom:#dbe7f4;
  --nav-top:#3cc0f4;
  --nav-bottom:#0d9be0;
  --side:#6e9fd6;
  --side-dark:#1b78c0;
  --side-line:#8fb6e2;
  --yellow:#f4e14a;
  --pink:#e33f74;
  --orange:#f5b400;
  --mid-blue:#3a8fd0;
  --green:#7cc242;
  --caption:#2a8ed6;
  --panel:#dce9f8;
  --ink:#1d3f78;
  --title-blue:#1a8fe0;
  --link-orange:#f08a00;
  --white:#ffffff;
}
*{box-sizing:border-box;margin:0;padding:0}
html,body{width:1200px;height:900px;overflow:hidden}
body{position:relative;font-family:"Arimo",Arial,sans-serif;color:var(--ink)}
.backdrop{position:absolute;inset:0;background:linear-gradient(180deg,var(--sky-top),var(--sky-bottom) 60%,#c8d9ee)}
.abs{position:absolute}
.event-date{left:200px;top:64px;font:italic 29px "Lora",Georgia,serif;color:var(--white)}
.corner-balloon{left:118px;top:60px;width:58px;height:76px;border-radius:50% 50% 45% 45%;background:linear-gradient(90deg,#f08a24,#e33f3f,#3a8fd0)}
.countdown{left:884px;top:66px;display:flex;gap:12px;align-items:flex-start}
.countdown .unit{font:700 12px "Arimo",sans-serif;line-height:14px}
.countdown .label{color:var(--yellow)}
.countdown .value{color:var(--white)}
.header{left:113px;top:100px;width:976px;height:221px;background:linear-gradient(180deg,#2ea6ee,#9fd2f5 55%,#e4f2fb);overflow:hidden}
.header svg{position:absolute;left:0;top:0}
.brand{left:26px;top:50px;font:700 50px "Arimo",sans-serif;color:var(--pink);letter-spacing:1px}
.subtitle{left:26px;top:106px;font:700 23px "Archivo Narrow",sans-serif;color:var(--title-blue)}
.tagline{left:548px;top:128px;font:700 28px "Arimo",sans-serif;color:var(--white);transform:rotate(8deg);transform-origin:left top;letter-spacing:1px;text-shadow:0 0 3px #0d6fc0;white-space:nowrap}
.nav{left:106px;top:321px;width:991px;height:39px;background:linear-gradient(180deg,var(--nav-top),var(--nav-bottom))}
.nav a{position:absolute;top:13px;font:700 12px "Arimo",sans-serif;color:var(--white);text-decoration:none;white-space:nowrap}
.main{left:113px;top:360px;width:976px;height:438px;background:var(--white)}
.sidebar{left:113px;top:360px;width:212px;height:438px;background:var(--side)}
.side-head{font:700 14px "Arimo",sans-serif;color:var(--yellow)}
.field-label{font:12px "Arimo",sans-serif;color:var(--white)}
.field{width:179px;height:22px;background:var(--white);border:1px solid #c9d9ee}
.btn{height:25px;border-radius:4px;background:linear-gradient(#fff,#e3e8ee);border:1px solid #b7c4d4;font:12px "Arimo",sans-serif;color:#223;display:flex;align-items:center;justify-content:center}
.forgot{font:700 11px "Arimo",sans-serif;color:#e9f1fb}
.new-user{left:113px;top:530px;width:212px;height:50px;background:var(--side-dark);padding:7px 18px;font:700 11px "Arimo",sans-serif;color:var(--white);line-height:17px}
.new-user u{font-weight:400;font-size:12px}
.quick{left:113px;top:614px;width:212px}
.quick li{list-style:none;height:30px;border-bottom:1px solid var(--side-line);padding:8px 0 0 18px;font:12px "Arimo",sans-serif;color:var(--white)}
.card{top:371px;width:177px;height:246px;border-radius:8px;overflow:hidden;background:var(--caption)}
.card .tab{height:24px;font:700 13.5px "Arimo",sans-serif;color:var(--white);text-align:center;line-height:24px}
.card .photo{height:142px}
.card .caption{position:absolute;left:0;top:166px;width:100%;height:80px;background:var(--caption);padding:12px 4px 0 17px;font:700 11.5px "Arimo",sans-serif;color:var(--white);line-height:18px}
.info{left:338px;top:628px;width:740px;height:162px;background:var(--panel);display:flex}
.col{position:relative;height:100%;border-right:1px solid var(--white)}
.col h2{position:absolute;left:11px;top:13px;font:400 16px "Arimo",sans-serif;color:var(--pink)}
.weather-table{position:absolute;left:11px;top:54px;font:11px "Arimo",sans-serif;color:var(--ink);border-collapse:collapse}
.weather-table td{height:17px;padding:0}
.weather-table td:first-child{font-weight:700;width:78px}
.more{position:absolute;left:11px;top:126px;font:11px "Arimo",sans-serif;color:var(--ink);text-decoration:underline}
.quick-action{position:absolute;left:8px;width:226px;height:40px;border-bottom:1px solid var(--white);display:flex;align-items:center;gap:10px;font:400 21px "Arimo",sans-serif;color:var(--ink)}
.social{position:absolute;top:126px;display:flex;gap:6px;font:700 11px "Arimo",sans-serif;color:var(--link-orange);line-height:14px}
.social .mark{width:23px;height:23px;background:#4a7fc8;border-radius:3px}
.copyright{left:113px;top:805px;font:12px "Arimo",sans-serif;color:#2a3f66}
</style>
</head>
<body>
<div class="backdrop" role="img" aria-label="Sky full of colourful hot air balloons with crowd in baskets below"></div>

<div class="abs corner-balloon" role="img" aria-label="Small striped hot air balloon"></div>
<div class="abs event-date">24th April 2011</div>

<div class="abs countdown">
  <svg width="28" height="28" viewBox="0 0 28 28"><circle cx="14" cy="14" r="12" fill="none" stroke="#fff" stroke-width="2.5"/><path d="M14 7v7l4 3" stroke="#fff" stroke-width="2" fill="none"/></svg>
  <div class="unit"><div class="label">DAYS</div><div class="value">65</div></div>
  <div class="unit"><div class="label">HOUR</div><div class="value">18</div></div>
  <div class="unit"><div class="label">MIN</div><div class="value">30</div></div>
  <div class="unit"><div class="label">SEC</div><div class="value">11</div></div>
</div>

<header class="abs header">
  <svg width="976" height="221" viewBox="0 0 976 221" role="img" aria-label="Close view of bright hot air balloons with fireworks">
    <defs><linearGradient id="hero" x1="0" y1="0" x2="1" y2="1"><stop offset="0" stop-color="#e8b52a"/><stop offset=".4" stop-color="#d8403a"/><stop offset=".75" stop-color="#2c6fc4"/><stop offset="1" stop-color="#49c8ef"/></linearGradient></defs>
    <path d="M400 221 C395 120 430 40 510 10 C600 -20 700 20 780 5 C850 -8 900 -20 976 -10 L976 221 Z" fill="url(#hero)"/>
    <path d="M400 221 C470 150 560 190 640 150 C730 105 830 190 976 150 L976 221 Z" fill="#fff" opacity=".9"/>
  </svg>
  <div class="abs brand">REDHOLLOW</div>
  <div class="abs subtitle">Annual Hot Air Balloon Festival</div>
  <div class="abs tagline">A UNIQUE EXPERIENCE</div>
</header>

<nav class="abs nav">
  <a href="#" style="left:26px">EVENT INFO ▼</a>
  <a href="#" style="left:130px">GUEST GUIDE ▼</a>
  <a href="#" style="left:241px">GAS BALLOONS ▼</a>
  <a href="#" style="left:366px">PILOTS AND CREW ▼</a>
  <a href="#" style="left:507px">BALLOONING ▼</a>
  <a href="#" style="left:616px">OPERATIONS ▼</a>
  <a href="#" style="left:727px">SPONSORS ▼</a>
  <a href="#" style="left:823px">MERCHANDISE</a>
  <a href="#" style="left:926px">MEDIA</a>
</nav>

<div class="abs main"></div>

<aside class="abs sidebar">
  <div class="abs side-head" style="left:16px;top:11px">LOGIN</div>
  <div class="abs field-label" style="left:16px;top:36px">User Name</div>
  <div class="abs field" style="left:16px;top:54px"></div>
  <div class="abs field-label" style="left:16px;top:84px">Password</div>
  <div class="abs field" style="left:16px;top:100px"></div>
  <div class="abs btn" style="left:16px;top:133px;width:72px">LOGIN ››</div>
  <div class="abs forgot" style="left:92px;top:139px">Forgot Password?</div>
  <div class="abs side-head" style="left:16px;top:231px">Quick Link</div>
</aside>

<div class="abs new-user">New User?<br><u>Click Here to Register</u></div>

<ul class="abs quick">
  <li>›› Attendees</li><li>›› Pilots</li><li>›› Vendors</li><li>›› Volunteers</li><li>›› Performers</li>
</ul>

<div class="abs card" style="left:337px">
  <div class="tab" style="background:var(--pink)">GUEST GUIDE</div>
  <div class="photo" role="img" aria-label="Pink and yellow balloon envelope" style="background:linear-gradient(135deg,#c9307a,#e7d24a 50%,#7a2c6a)"></div>
  <div class="caption">Everything you'll need to enjoy the Balloon Jubilee, Click Here!</div>
</div>
<div class="abs card" style="left:524px">
  <div class="tab" style="background:var(--orange)">BUY A BRICK</div>
  <div class="photo" role="img" aria-label="Balloons inflating on the field" style="background:linear-gradient(160deg,#cfe1f3,#e8523a 45%,#f3c21c)"></div>
  <div class="caption">Make a lasting memory at Balloon Jubilee Park with your own brick!</div>
</div>
<div class="abs card" style="left:713px">
  <div class="tab" style="background:var(--mid-blue)">MERCHANDISE</div>
  <div class="photo" role="img" aria-label="Skydiver with a flag against the sky" style="background:linear-gradient(180deg,#f3f6fa,#c9dcef)"></div>
  <div class="caption">Click here for official Bal-loon Jubilee gear at updraftgear.com!</div>
</div>
<div class="abs card" style="left:901px">
  <div class="tab" style="background:var(--green)">RV INFORMATION</div>
  <div class="photo" role="img" aria-label="Cooks preparing food at an outdoor grill" style="background:linear-gradient(160deg,#8a8f96,#c9b59a 55%,#6d5a48)"></div>
  <div class="caption">Accepting RV reservations for the 2011 Balloon Jubilee!</div>
</div>

<section class="abs info">
  <div class="col" style="width:238px">
    <h2>WEATHER</h2>
    <svg class="abs" style="left:128px;top:6px" width="48" height="44" viewBox="0 0 48 44"><circle cx="20" cy="18" r="12" fill="#f7c531"/><ellipse cx="28" cy="32" rx="16" ry="9" fill="#fff"/></svg>
    <table class="weather-table">
      <tr><td>Updated</td><td>02/17/11 3:36a</td></tr>
      <tr><td>Temperature:</td><td>49.0F</td></tr>
      <tr><td>Wind:</td><td>2.0 mph From S (176 Deg.)</td></tr>
    </table>
    <div class="more">Click here for more detailed info</div>
  </div>
  <div class="col" style="width:259px">
    <h2>FREE NEWSLETTER</h2>
    <svg class="abs" style="left:178px;top:8px" width="42" height="30" viewBox="0 0 42 30"><rect x="1" y="1" width="40" height="28" fill="#f4f4f4" stroke="#bbb"/><path d="M1 1l20 16L41 1" fill="none" stroke="#bbb"/></svg>
    <div class="abs" style="left:11px;top:53px;font:700 11px Arimo,sans-serif">Enter your email id:</div>
    <div class="abs field" style="left:11px;top:72px;width:162px;height:23px"></div>
    <div class="abs btn" style="left:11px;top:105px;width:111px">SUBSCRIBE ››</div>
  </div>
  <div class="col" style="width:243px;border:none">
    <div class="quick-action" style="top:0"><svg width="30" height="26" viewBox="0 0 30 26"><rect x="3" y="6" width="24" height="14" rx="2" fill="#eee" stroke="#999" transform="rotate(-25 15 13)"/></svg>Ticket</div>
    <div class="quick-action" style="top:40px"><svg width="30" height="28" viewBox="0 0 30 28"><rect x="2" y="3" width="26" height="23" rx="2" fill="#fff" stroke="#888"/><rect x="2" y="3" width="26" height="6" fill="#999"/><text x="15" y="22" font-size="11" text-anchor="middle" fill="#333" font-family="Arimo">12</text></svg>Event Schedule</div>
    <div class="quick-action" style="top:80px"><svg width="30" height="26" viewBox="0 0 30 26"><circle cx="13" cy="13" r="11" fill="#ccc" stroke="#777"/><circle cx="13" cy="13" r="3" fill="#777"/><rect x="22" y="10" width="7" height="10" fill="#888"/></svg>Launch Video</div>
    <div class="social" style="left:14px"><span class="mark"></span><span>Join us on<br>Friendhub</span></div>
    <div class="social" style="left:118px"><span class="mark" style="background:#5cb8e8"></span><span>Follow us on<br>Chirper</span></div>
  </div>
</section>

<footer class="abs copyright">© 2011 redhollowfest.com . All rights reserved.</footer>
</body>
</html>
```